Banner Designs for Drone Defense Ad Campaign

Harborlyte is a security consulting and services company that offers a service called SkyMarrowin. SkyMarrowin helps our customers identify security risks from drones and develops comprehensive protection programs. We are looking for a designer to create a banner ad in three sizes for our campaign.
Target Market(s)
Our campaign is geared to the sports and entertainment industry, specifically large event venues and their security operation.
Industry/Entity Type
Security
Font styles to use
Other font styles liked:
- Raleway
Requirements
Must have
- Banner Objective
The visual and textual content of the banner should prompt the viewer to quickly identify the service offered and the information that is available to download.
Banner Design
Logo: SkyMarrowin logo
Call to Action Button in Red: Get It Here (On Right or or Upper Right)
Title in Larger Font: Guide to UAS Risk Mitigation
Subtitle in smaller Font: 5 Steps to Develop Your Comprehensive UAS Defense Program
Background: Stadium with a drone flying in foreground
Font: Raleway
Banner Sizes
1 - 1200x670 pixels
2 - 1510x196 pixels
3 - 1200x628 pixels

```html
<!DOCTYPE html>
<html lang="en">
<head>
<meta charset="utf-8">
<title>Drone Defense Banner Set</title>
<link rel="stylesheet" href="https://fonts.googleapis.com/css2?family=Raleway:wght@400;500;600;800&display=swap">
<style>
  :root {
    --sheet: #b3b3b3;
    --ink: #1e1e1e;
    --night: #050816;
    --night-2: #0a1024;
    --brand-blue: #2f80d9;
    --white: #ffffff;
    --soft-white: #e9ecf2;
    --cta-red: #d60a0a;
  }
  * { box-sizing: border-box; margin: 0; padding: 0; }
  html, body { width: 804px; height: 1200px; overflow: hidden; }
  body {
    position: relative;
    background: var(--sheet);
    font-family: "Raleway", sans-serif;
    color: var(--ink);
  }
  .sheet-title {
    position: absolute; top: 48px; left: 0; width: 804px;
    text-align: center; font-size: 21px; font-weight: 400; letter-spacing: 0.2px;
  }
  .size-label {
    position: absolute; left: 53px; font-size: 13px; font-weight: 500;
  }
  .banner {
    position: absolute; left: 53px; overflow: hidden;
    box-shadow: 0 2px 5px rgba(0,0,0,0.35);
    background: var(--night);
  }
  .banner-photo { position: absolute; inset: 0; }
  .photo-arena-dusk {
    background:
      radial-gradient(ellipse 40% 30% at 78% 10%, rgba(232,128,60,0.75), transparent 70%),
      radial-gradient(ellipse 45% 35% at 75% 80%, rgba(110,80,200,0.55), transparent 70%),
      radial-gradient(ellipse 40% 25% at 72% 55%, rgba(60,80,120,0.8), transparent 70%),
      linear-gradient(90deg, var(--night) 0%, var(--night) 30%, #141d38 60%, #1c2746 100%);
  }
  .photo-arena-pitch {
    background:
      radial-gradient(ellipse 35% 45% at 72% 70%, rgba(82,160,60,0.95), transparent 75%),
      radial-gradient(ellipse 20% 25% at 88% 25%, rgba(200,200,210,0.55), transparent 70%),
      linear-gradient(90deg, var(--night) 0%, var(--night) 35%, #1c2420 62%, #2a3a2a 100%);
  }
  .photo-arena-strip {
    background:
      radial-gradient(ellipse 16% 60% at 80% 80%, rgba(100,80,200,0.5), transparent 70%),
      linear-gradient(90deg, var(--night-2) 0%, var(--night-2) 65%, #1b2644 100%);
  }
  .brand { position: absolute; }
  .brand-name {
    display: block; font-weight: 600; color: var(--brand-blue); line-height: 1;
  }
  .brand-parent {
    display: block; text-align: right; color: var(--soft-white); font-weight: 500; margin-top: 3px;
  }
  .headline { position: absolute; color: var(--white); }
  .headline-lead { display: block; font-weight: 400; line-height: 1; }
  .headline-main {
    display: block; font-weight: 800; color: var(--brand-blue);
    line-height: 0.9; letter-spacing: -1.5px;
  }
  .headline-sub { display: block; font-weight: 500; color: var(--white); }
  .cta-ribbon { position: absolute; top: 0; right: 0; }
  .cta-ribbon text {
    font-family: "Raleway", sans-serif; font-weight: 800; fill: var(--white);
  }

  /* Large 1200x670 */
  .banner-large { top: 136px; width: 701px; height: 393px; }
  .banner-large .brand { left: 34px; top: 48px; }
  .banner-large .brand-name { font-size: 23px; }
  .banner-large .brand-parent { font-size: 12px; }
  .banner-large .headline { left: 42px; top: 124px; }
  .banner-large .headline-lead { font-size: 46px; }
  .banner-large .headline-main { font-size: 58px; margin-top: 4px; }
  .banner-large .headline-sub { font-size: 18px; line-height: 28px; margin-top: 20px; }

  /* Medium 1200x628 */
  .banner-medium { top: 595px; width: 698px; height: 366px; }
  .banner-medium .brand { left: 32px; top: 54px; }
  .banner-medium .brand-name { font-size: 21px; }
  .banner-medium .brand-parent { font-size: 11px; }
  .banner-medium .headline { left: 38px; top: 124px; }
  .banner-medium .headline-lead { font-size: 42px; }
  .banner-medium .headline-main { font-size: 53px; margin-top: 4px; }
  .banner-medium .headline-sub { font-size: 17px; line-height: 26px; margin-top: 16px; }

  /* Leaderboard 1510x196 */
  .banner-strip { top: 1047px; width: 695px; height: 90px; }
  .banner-strip .brand { left: 18px; top: 24px; }
  .banner-strip .brand-name { font-size: 17px; }
  .banner-strip .brand-parent { font-size: 9px; margin-top: 2px; }
  .banner-strip .headline { left: 168px; top: 9px; width: 300px; text-align: center; }
  .banner-strip .headline-lead { font-size: 19px; }
  .banner-strip .headline-main { font-size: 26px; letter-spacing: -0.5px; margin-top: 3px; white-space: nowrap; }
  .banner-strip .headline-sub { font-size: 10px; margin-top: 6px; white-space: nowrap; }
</style>
</head>
<body>
  <h1 class="sheet-title">Banner Designs for Drone Defense Ad Campaign</h1>

  <section class="banner banner-large">
    <div class="banner-photo photo-arena-dusk" role="img" aria-label="Aerial view of a lit stadium at dusk over a city, with a white quadcopter drone flying in the foreground"></div>
    <div class="brand">
      <span class="brand-name">SkyMarrowin</span>
      <span class="brand-parent">By Harborlyte</span>
    </div>
    <div class="headline">
      <span class="headline-lead">GUIDE TO</span>
      <span class="headline-main">UAS RISK<br>MITIGATION</span>
      <span class="headline-sub">5 Steps to Develop Your<br>Comprehensive UAS Defense Program</span>
    </div>
    <svg class="cta-ribbon" width="131" height="124" viewBox="0 0 131 124">
      <polygon points="0,0 131,0 131,124" fill="var(--cta-red)"/>
      <g transform="translate(83,42) rotate(43)">
        <text x="0" y="-2" font-size="14" text-anchor="middle">DOWNLOAD</text>
        <text x="-14" y="14" font-size="14" text-anchor="middle">NOW</text>
      </g>
    </svg>
  </section>
  <p class="size-label" style="top:540px">1200X670</p>

  <section class="banner banner-medium">
    <div class="banner-photo photo-arena-pitch" role="img" aria-label="Aerial night view of a packed football stadium with a green pitch and smoke, a white quadcopter drone hovering above the stands"></div>
    <div class="brand">
      <span class="brand-name">SkyMarrowin</span>
      <span class="brand-parent">By Harborlyte</span>
    </div>
    <div class="headline">
      <span class="headline-lead">GUIDE TO</span>
      <span class="headline-main">UAS RISK<br>MITIGATION</span>
      <span class="headline-sub">5 Steps to Develop Your<br>Comprehensive UAS Defense Program</span>
    </div>
    <svg class="cta-ribbon" width="125" height="108" viewBox="0 0 125 108">
      <polygon points="0,0 125,0 125,108" fill="var(--cta-red)"/>
      <g transform="translate(80,38) rotate(41)">
        <text x="0" y="-2" font-size="13.5" text-anchor="middle">DOWNLOAD</text>
        <text x="-14" y="14" font-size="13.5" text-anchor="middle">NOW</text>
      </g>
    </svg>
  </section>
  <p class="size-label" style="top:976px">1200X628</p>

  <section class="banner banner-strip">
    <div class="banner-photo photo-arena-strip" role="img" aria-label="Lit stadium at night seen from above with a white quadcopter drone flying overhead"></div>
    <div class="brand">
      <span class="brand-name">SkyMarrowin</span>
      <span class="brand-parent">By Harborlyte</span>
    </div>
    <div class="headline">
      <span class="headline-lead">GUIDE TO</span>
      <span class="headline-main">UAS RISK&nbsp; MITIGATION</span>
      <span class="headline-sub">5 Steps to Develop Your&nbsp; Comprehensive UAS Defense Program</span>
    </div>
    <svg class="cta-ribbon" width="90" height="90" viewBox="0 0 90 90">
      <polygon points="0,0 90,0 90,86" fill="var(--cta-red)"/>
      <g transform="translate(58,32) rotate(44)">
        <text x="0" y="-2" font-size="10" text-anchor="middle">DOWNLOAD</text>
        <text x="-10" y="10" font-size="10" text-anchor="middle">NOW</text>
      </g>
    </svg>
  </section>
  <p class="size-label" style="top:1155px">1510X196</p>
</body>
</html>
```